Funeral Services Site

We need a website for a Funeral Services company. The old website is: www.rouwcentrumkorvelaer.be We need the same structure and text.

Target Market(s)

Customers.

Coding

Coded - Design and coding required

Number of Pages Required

4 page

Font styles to use
Serif
Sans Serif
Script

```html
<!DOCTYPE html>
<html lang="nl">
<head>
<meta charset="utf-8">
<title>Rouwcentrum Korvelaer</title>
<link href="https://fonts.googleapis.com/css2?family=Great+Vibes&family=Playfair+Display:wght@400;700&family=Open+Sans:wght@400;600;700&display=swap" rel="stylesheet">
<style>
:root{
  --ink:#2b2b2b;
  --text:#555;
  --muted:#888;
  --green:#8cc63f;
  --dark:#1f1c19;
  --darker:#141210;
  --grey-bg:#f4f4f4;
  --line:#dcdcdc;
  --white:#fff;
}
*{box-sizing:border-box;margin:0;padding:0}
html,body{width:1200px;height:2248px;overflow:hidden}
body{font-family:"Open Sans",Arial,sans-serif;color:var(--text);background:var(--white);font-size:13px;line-height:1.6}
.brand{font-family:"Playfair Display",Georgia,serif;font-weight:400;color:var(--ink)}

.topbar{height:14px;background:var(--darker)}
.topbar .inner{width:1000px;margin:0 auto;display:flex;justify-content:flex-end;gap:10px;color:#ccc;font-size:8px;line-height:14px}

.nav{height:68px;display:flex;align-items:center;justify-content:center;gap:26px;border-bottom:1px solid #eee}
.nav a{font-size:10px;text-transform:uppercase;color:var(--ink);text-decoration:none;letter-spacing:.5px}
.nav a.active{color:var(--green);border-bottom:2px solid var(--green);padding-bottom:2px}
.nav .logo{font-size:17px;line-height:1.05;text-align:center;margin:0 30px}
.nav .cta{background:var(--green);color:var(--white);padding:7px 18px;border-radius:2px}

.hero{position:relative;height:318px;overflow:hidden}
.hero .photo{position:absolute;inset:0;background:linear-gradient(90deg,#2a2420 0%,#4a3f36 45%,#5b4e43 60%,#2a2420 100%)}
.hero .content{position:relative;text-align:center;color:var(--white);padding-top:28px}
.hero h1{font-family:"Great Vibes",cursive;font-weight:400;font-size:40px;line-height:1.1}
.hero .phone{display:inline-flex;align-items:center;gap:18px;margin-top:30px;border:2px solid var(--white);padding:14px 34px;font-size:52px;font-weight:600;letter-spacing:2px}
.hero .dots{position:absolute;bottom:18px;left:0;right:0;display:flex;justify-content:center;gap:6px}
.hero .dots span{width:8px;height:8px;border-radius:50%;border:1px solid var(--white)}
.hero .dots span.on{background:var(--white)}

.about{height:342px;text-align:center;padding-top:42px}
.about .brand{font-size:34px;line-height:1}
.about .sub{font-size:13px;color:var(--ink);margin-top:4px}
.about h2{font-size:14px;font-weight:700;color:var(--ink);margin:14px 0 10px}
.about p{width:720px;margin:0 auto 10px;font-size:11px}

.organisatie{height:498px;background:var(--grey-bg);text-align:center;padding-top:46px}
.heading{font-family:"Playfair Display",Georgia,serif;font-weight:400;font-size:26px;color:var(--ink);line-height:1.2}
.rule{width:60px;height:2px;background:var(--green);margin:12px auto 18px}
.organisatie p{width:700px;margin:0 auto 8px;font-size:11px}
.features{display:flex;justify-content:center;gap:20px;margin-top:44px}
.feature{position:relative;width:220px;height:170px;background:var(--white);border:1px solid var(--line);padding:44px 18px 0;text-align:left}
.feature .ico{position:absolute;top:-18px;left:92px;width:36px;height:36px;border-radius:50%;background:var(--green);display:flex;align-items:center;justify-content:center}
.feature h3{font-family:"Playfair Display",Georgia,serif;font-weight:700;font-size:17px;color:var(--ink);line-height:1.25}

.testimonials{height:322px;text-align:center;padding-top:50px}
.testimonials .quote{font-family:"Playfair Display",Georgia,serif;font-size:44px;color:var(--green);line-height:1;margin-top:6px}
.testimonials p{width:460px;margin:6px auto 18px;font-size:11px}
.person{display:inline-flex;align-items:center;gap:12px}
.person .avatar{width:36px;height:36px;border-radius:50%;background:linear-gradient(#c9b39b,#8c7560)}
.person .who{text-align:left;font-size:10px;line-height:1.3}
.person .who b{display:block;color:var(--ink)}

.contact{height:440px;border-top:1px solid #eee;text-align:center;padding-top:46px}
.form{width:420px;margin:0 auto;display:grid;grid-template-columns:1fr 1fr;gap:10px 20px;text-align:left}
.form label{display:block;font-size:9px;color:var(--muted);margin-bottom:3px}
.form .field{height:26px;border:1px solid var(--line)}
.form .full{grid-column:1/3}
.form .area{height:80px;border:1px solid var(--line)}
.form .send{grid-column:1/3;justify-self:center;margin-top:14px;background:var(--green);color:var(--white);font-size:10px;font-weight:700;padding:8px 46px;border-radius:2px;text-transform:uppercase}

.footer{height:220px;background:var(--dark);color:#bbb}
.footer .inner{width:1000px;margin:0 auto;display:flex;gap:60px;padding-top:34px}
.footer .brand{color:var(--white);font-size:26px;line-height:1.1;width:260px}
.social{display:flex;gap:10px;margin-top:18px}
.social span{width:12px;height:12px;border-radius:50%;background:#777}
.footer .info{width:260px;font-size:10px}
.footer .info div{display:flex;align-items:center;gap:10px;margin-bottom:12px}
.footer .info .ic{width:26px;height:26px;border:1px solid #555;display:flex;align-items:center;justify-content:center}
.footer .about-text{width:330px;font-size:10px;line-height:1.7}
.bottombar{height:28px;background:var(--darker);color:#888;font-size:8px}
.bottombar .inner{width:1000px;margin:0 auto;display:flex;justify-content:space-between;line-height:28px}
</style>
</head>
<body>

<div class="topbar"><div class="inner"><span>013 28 40 61</span><span>info@rouwcentrumkorvelaer.be</span></div></div>

<nav class="nav">
  <a class="active" href="#">Home</a>
  <a href="#">Over ons</a>
  <a href="#">Onze diensten</a>
  <div class="logo brand">Rouwcentrum<br>Korvelaer</div>
  <a href="#">Rouwcentrum</a>
  <a href="#">Contact</a>
  <a class="cta" href="#">013 28 40 61</a>
</nav>

<section class="hero">
  <div class="photo" role="img" aria-label="Sfeerfoto van een rustige aula met kaarsen en bloemen"></div>
  <div class="content">
    <h1>Rouwcentrum Korvelaer biedt:<br>een persoonlijke service in uitvaartbegeleiding</h1>
    <div class="phone">
      <svg width="44" height="44" viewBox="0 0 24 24" fill="#fff"><path d="M6.6 10.8a15.1 15.1 0 0 0 6.6 6.6l2.2-2.2c.3-.3.7-.4 1-.2 1.1.4 2.3.6 3.6.6.6 0 1 .4 1 1V20c0 .6-.4 1-1 1A17 17 0 0 1 3 4c0-.6.4-1 1-1h3.5c.6 0 1 .4 1 1 0 1.3.2 2.5.6 3.6.1.3 0 .7-.2 1z"/></svg>
      013 28 40 61
    </div>
  </div>
  <div class="dots"><span class="on"></span><span></span><span></span></div>
</section>

<section class="about">
  <div class="brand">Rouwcentrum Korvelaer</div>
  <div class="sub">Voor complete service in rouw- en uitvaartbegeleiding</div>
  <h2>OVER ONS:</h2>
  <p>Wanneer iemand van wie u houdt overlijdt, staat u voor vele beslissingen. Ons team begeleidt u met zorg en respect in elke stap van het afscheid. Wij nemen de tijd om te luisteren en zorgen voor een <b>waardig en persoonlijk afscheid</b> dat past bij uw dierbare.</p>
  <p>Sinds meer dan twintig jaar staan wij klaar met <b>ondersteuning en uitvaartbegeleiding</b>, dag en nacht bereikbaar, <b>24 uur op 24 en 7 dagen op 7</b>. Ons familiebedrijf kent de regio en werkt met vertrouwde partners.</p>
</section>

<section class="organisatie">
  <h2 class="heading">Organisatie uitvaart en<br>rouwdienst</h2>
  <div class="rule"></div>
  <p>Wij regelen alle praktische zaken van de uitvaart, van de eerste melding tot de laatste groet. Samen met u bespreken wij de wensen voor de dienst, de bloemen, de muziek en de <b>locatie van de plechtigheid</b>, zodat alles verloopt zoals u het wenst.</p>
  <p>Wij zorgen ook voor de administratie, de rouwbrieven en de contacten met de gemeente en de kerk.</p>
  <div class="features">
    <div class="feature">
      <div class="ico"><svg width="16" height="16" viewBox="0 0 24 24" fill="none" stroke="#fff" stroke-width="3"><path d="M4 12l5 5L20 6"/></svg></div>
      <h3>geborduurde afscheid voor de begrafenis</h3>
    </div>
    <div class="feature">
      <div class="ico"><svg width="16" height="16" viewBox="0 0 24 24" fill="none" stroke="#fff" stroke-width="3"><path d="M4 12l5 5L20 6"/></svg></div>
      <h3>gebondelde met priester (indien mogelijk)</h3>
    </div>
    <div class="feature">
      <div class="ico"><svg width="16" height="16" viewBox="0 0 24 24" fill="none" stroke="#fff" stroke-width="3"><path d="M4 12l5 5L20 6"/></svg></div>
      <h3>uitvaartdienst met priester (op dinsdag en vrijdag in de parochie van Korvel)</h3>
    </div>
  </div>
</section>

<section class="testimonials">
  <h2 class="heading" style="font-size:20px">What Our Families Say</h2>
  <div class="rule" style="margin-bottom:6px"></div>
  <div class="quote">&ldquo;&ldquo;</div>
  <p>Het team stond ons in de moeilijkste dagen met raad en daad bij. Alles werd met zorg geregeld en het afscheid was precies zoals mama het gewild zou hebben. Onze oprechte dank.</p>
  <div class="person">
    <div class="avatar" role="img" aria-label="Portretfoto van de familie"></div>
    <div class="who"><b>Lieve Maes</b>Familie</div>
  </div>
</section>

<section class="contact">
  <h2 class="heading" style="font-size:20px">Contact Us for Urgent Help</h2>
  <div class="rule"></div>
  <div class="form">
    <div><label>Voornaam</label><div class="field"></div></div>
    <div><label>Achternaam</label><div class="field"></div></div>
    <div><label>E-mail</label><div class="field"></div></div>
    <div><label>Telefoon</label><div class="field"></div></div>
    <div class="full"><label>Bericht</label><div class="area"></div></div>
    <div class="send">Send</div>
  </div>
</section>

<footer class="footer">
  <div class="inner">
    <div>
      <div class="brand">Rouwcentrum<br>Korvelaer</div>
      <div class="social"><span></span><span></span><span></span></div>
    </div>
    <div class="info">
      <div><span class="ic"><svg width="12" height="12" viewBox="0 0 24 24" fill="#8cc63f"><path d="M6.6 10.8a15.1 15.1 0 0 0 6.6 6.6l2.2-2.2c.3-.3.7-.4 1-.2 1.1.4 2.3.6 3.6.6.6 0 1 .4 1 1V20c0 .6-.4 1-1 1A17 17 0 0 1 3 4c0-.6.4-1 1-1h3.5c.6 0 1 .4 1 1 0 1.3.2 2.5.6 3.6.1.3 0 .7-.2 1z"/></svg></span>013 28 40 61</div>
      <div><span class="ic"><svg width="12" height="12" viewBox="0 0 24 24" fill="#8cc63f"><path d="M12 2a7 7 0 0 0-7 7c0 5 7 13 7 13s7-8 7-13a7 7 0 0 0-7-7zm0 9.5A2.5 2.5 0 1 1 12 6.5a2.5 2.5 0 0 1 0 5z"/></svg></span>Lindestraat 14, 3500 Korvel</div>
      <div><span class="ic"><svg width="12" height="12" viewBox="0 0 24 24" fill="none" stroke="#8cc63f" stroke-width="2"><rect x="3" y="5" width="18" height="14"/><path d="M3 6l9 7 9-7"/></svg></span>info@rouwcentrumkorvelaer.be</div>
    </div>
    <div class="about-text">Rouwcentrum Korvelaer is een familiebedrijf dat families begeleidt bij het afscheid van een dierbare. Met respect, rust en aandacht voor elk detail zorgen wij voor een persoonlijke uitvaart. U kunt ons dag en nacht bereiken voor advies en hulp.</div>
  </div>
</footer>
<div class="bottombar"><div class="inner"><span>Copyright &copy; Rouwcentrum Korvelaer</span><span>Privacybeleid &nbsp;&nbsp; Disclaimer</span></div></div>

</body>
</html>
```